Buch-/eBook-Cover für Liebesroman
Zielgruppe
Ich bin Autorin und suche ein Cover für mein neues Buch. Meine Zielgruppe sind junge Erwachsene, die Liebesromane lesen.
Aufgabenstellung
Der Titel ist 'Als ob ein Regen durch die Stille fällt' und als Autorin soll Margarete Hollweck draufstehen.
Ich mag Cover, auf denen keine Menschen bzw. nicht der komplette Mensch zu sehen ist. Farbentechnisch würde ich mich überraschen lassen, solange es nicht zu bunt wird. :-) Als Schriftart darf es gern eine Schreibschrift sein. Ich lasse mich aber auch zu etwas anderem überreden, wenn es zum restlichen Cover passt. ;-)
Das Cover sollte eine Auflösung von mind. 300 dpi haben (gern mehr) und möglichst im jpg-Format sein.
Der Inhalt des Buches: Es geht um ein Männerpaar. Der eine ist verheiratet (mit einer Frau) und verliebt sich in seinen Kumpel. Die beiden beginnen eine Affäre, woraus aber bald mehr wird. Am Ende trennt er sich von seiner Frau und entscheidet sich für seinen Kumpel.
Es ist ein Liebesroman, aber das Cover sollte trotzdem nicht zu klischeehaft sein.
Da ich das hier nicht anders auswählen kann, noch eine kleine Anmerkung. Ich möchte nach Möglichkeit keine Stockmaterialien im Cover haben.

```html
<!DOCTYPE html>
<html lang="de">
<head>
<meta charset="utf-8">
<title>Als ob ein Regen durch die Stille fällt – Margarete Hollweck</title>
<link rel="stylesheet" href="https://fonts.googleapis.com/css2?family=Roboto+Slab:wght@400&family=Allison&display=swap">
<style>
  :root {
    --paper: #f2f2f2;
    --ink: #111111;
    --rose: #d48a8a;
    --peach: #f5dfcc;
    --sand: #f0d8b8;
    --salmon: #f0a898;
    --blush: #f9c9bf;
    --blush-deep: #f2c6bd;
  }
  html, body {
    margin: 0;
    padding: 0;
    overflow: hidden;
    background: var(--paper);
  }
  .cover {
    position: relative;
    width: 848px;
    height: 1200px;
    overflow: hidden;
    background: var(--paper);
  }
  .cover__art {
    position: absolute;
    inset: 0;
    width: 848px;
    height: 1200px;
  }
  .cover__author {
    position: absolute;
    top: 86px;
    left: 0;
    width: 848px;
    margin: 0;
    text-align: center;
    font-family: "Roboto Slab", Georgia, serif;
    font-weight: 400;
    font-size: 29px;
    letter-spacing: 0.2em;
    color: var(--ink);
    text-transform: uppercase;
  }
  .cover__title {
    margin: 0;
    font-weight: 400;
  }
  .title__lead,
  .title__tail {
    position: absolute;
    font-family: "Roboto Slab", Georgia, serif;
    font-size: 30px;
    letter-spacing: 0.18em;
    color: var(--ink);
    text-transform: uppercase;
    white-space: nowrap;
  }
  .title__lead {
    left: 132px;
    top: 790px;
  }
  .title__script {
    position: absolute;
    left: 0;
    width: 848px;
    top: 800px;
    text-align: center;
    font-family: "Allison", cursive;
    font-size: 250px;
    line-height: 1;
    color: var(--rose);
    white-space: nowrap;
  }
  .title__tail {
    right: 104px;
    top: 1118px;
  }
</style>
</head>
<body>
<main class="cover">
  <svg class="cover__art" viewBox="0 0 848 1200" xmlns="http://www.w3.org/2000/svg" aria-hidden="false">
    <defs>
      <radialGradient id="illustration-tone" cx="50%" cy="45%" r="55%">
        <stop offset="0%" stop-color="#ee9c84" stop-opacity="0.55"/>
        <stop offset="60%" stop-color="#f0c8b0" stop-opacity="0.35"/>
        <stop offset="100%" stop-color="#f2f2f2" stop-opacity="0"/>
      </radialGradient>
    </defs>

    <g class="backdrop-blobs">
      <path fill="var(--peach)" opacity="0.9"
        d="M0 502 C70 492 150 520 180 590 C200 650 210 680 250 700 C280 715 275 760 230 766 C170 772 110 740 60 748 C30 752 10 760 0 764 Z"/>
      <path fill="var(--blush)" opacity="0.75"
        d="M40 490 C90 470 170 485 210 520 C240 550 210 600 150 602 C90 604 30 590 29 560 C28 530 30 500 40 490 Z"/>
      <path fill="var(--blush-deep)" opacity="0.85"
        d="M848 480 L848 773 C830 760 820 730 818 700 C815 670 790 650 760 630 C735 610 735 560 760 520 C780 490 820 478 848 480 Z"/>
      <path fill="var(--peach)" opacity="0.85"
        d="M848 672 L848 910 C800 912 750 890 725 850 C702 812 708 760 740 722 C770 690 810 676 848 672 Z"/>
      <path fill="var(--sand)" opacity="0.9"
        d="M495 152 C540 150 575 190 565 250 C555 300 575 330 600 370 C630 420 625 460 580 490 C540 518 480 530 440 520 C400 505 395 450 398 400 C402 330 410 270 430 220 C448 180 470 154 495 152 Z"/>
      <path fill="var(--salmon)" opacity="0.85"
        d="M300 322 C360 312 420 340 470 390 C515 440 530 500 515 560 C500 600 460 605 430 592 C405 580 398 545 370 530 C330 515 270 530 245 480 C225 440 235 380 255 350 C268 333 282 325 300 322 Z"/>
    </g>

    <ellipse class="illustration-placeholder" role="img"
      aria-label="Feine Einlinienzeichnung: ein Schmetterling schwebt über einer geöffneten Hand"
      cx="515" cy="520" rx="340" ry="350" fill="url(#illustration-tone)"/>
  </svg>

  <p class="cover__author">Margarete Hollweck</p>

  <h1 class="cover__title">
    <span class="title__lead">Als ob ein</span>
    <span class="title__script">Regen</span>
    <span class="title__tail">durch die Stille fällt</span>
  </h1>
</main>
</body>
</html>
```